I would love for my business card to be fun and sophisicated. The clients are people that could afford nice well crafted wigs. These wigs are not like granny wigs. The're for women who are stylish and what to look there best especially if they are dealing with cancer are some from of hair loss. Do not want the card to appear crowded with to much information. If I need to eliminate some data, let me know.
Thanks

Industry/Entity Type

Hair

Contact Information for Business Card

L Radiant Tresses, Marjorie Ellison, owner, stylist

Wigs/Studio Showroom
Extensions
Hair Replacement
Private Room

24683 Mesa Vista Loop, Suite. R
Irvine, CA 90871
(949) 555-0178
Email: tresses@lradianttresses-example.com
www.lradianttresses-example.com

```html
<!DOCTYPE html>
<html lang="en">
<head>
<meta charset="utf-8">
<title>L Radiant Tresses – Business Card</title>
<link rel="stylesheet" href="https://fonts.googleapis.com/css2?family=Baskervville:ital@0;1&display=swap">
<style>
  :root {
    --page: #ffffff;
    --plum: #6e1470;
    --mint: #aadcd6;
    --ink: #2b2d5e;
    --coral: #e63c2f;
    --white: #ffffff;
    --hair-pink: #ec1a52;
    --hair-gold: #fbb829;
    --hair-rose: #e5509a;
  }
  * { margin: 0; padding: 0; box-sizing: border-box; }
  html, body {
    width: 1200px;
    height: 703px;
    overflow: hidden;
    background: var(--page);
  }
  .card {
    position: relative;
    width: 1200px;
    height: 703px;
    font-family: "Baskervville", "Baskerville", Georgia, serif;
    color: var(--ink);
  }
  .card-background {
    position: absolute;
    inset: 0;
  }
  .brand-name {
    position: absolute;
    left: 168px;
    top: 118px;
    font-size: 52px;
    font-weight: 400;
    color: var(--coral);
    letter-spacing: 0.5px;
    white-space: nowrap;
  }
  .services {
    position: absolute;
    left: 50px;
    top: 284px;
    font-size: 21px;
    font-style: italic;
    color: var(--white);
    white-space: nowrap;
  }
  .services .dot { margin: 0 6px; }
  .owner-name {
    position: absolute;
    left: 64px;
    top: 398px;
    font-size: 38px;
    font-weight: 400;
    letter-spacing: 0.5px;
    text-transform: uppercase;
  }
  .owner-role {
    position: absolute;
    left: 66px;
    top: 450px;
    font-size: 28px;
    font-style: italic;
  }
  .address, .contact {
    position: absolute;
    top: 530px;
    font-size: 23px;
    line-height: 39px;
    font-style: normal;
  }
  .address { left: 64px; }
  .contact { right: 400px; text-align: right; }
</style>
</head>
<body>
  <main class="card">
    <svg class="card-background" width="1200" height="703" viewBox="0 0 1200 703" aria-hidden="false">
      <rect class="mint-field" x="22" y="24" width="1158" height="660" fill="var(--mint)"/>
      <path class="plum-band" d="M22 24 H1180 V511 H900 V380 H22 Z" fill="var(--plum)"/>
      <defs>
        <linearGradient id="hair-tones" x1="0" y1="0" x2="1" y2="1">
          <stop offset="0" stop-color="var(--hair-gold)"/>
          <stop offset="0.45" stop-color="var(--hair-pink)"/>
          <stop offset="1" stop-color="var(--hair-gold)"/>
        </linearGradient>
      </defs>
      <rect class="hair-illustration" role="img"
            aria-label="Stylised illustration of flowing pink and golden hair"
            x="830" y="80" width="350" height="570" rx="120" fill="url(#hair-tones)"/>
    </svg>

    <h1 class="brand-name">L Radiant Tresses</h1>

    <p class="services">Wigs/Studio Showroom<span class="dot">•</span>Extension<span class="dot">•</span>Hair Replacement Private Room</p>

    <h2 class="owner-name">Marjorie Ellison</h2>
    <p class="owner-role">Owner / Stylist</p>

    <address class="address">
      24683 Mesa Vista Loop,<br>
      Suite R, Irvine<br>
      CA 90871
    </address>

    <address class="contact">
      (949) 555-0178<br>
      tresses@lradianttresses-example.com<br>
      www.lradianttresses-example.com
    </address>
  </main>
</body>
</html>
```